Tallowreed Advisory Partners Business Card Design

We have the logo we just need someone to design a modern business card design.

Name: Desmond Munkalt
Phone: 3055550148
Mobile: 9175550193
Web:www.tallowreedadvisory.example
email: dmunkalt@tallowreedadvisory.example
Company: Tallowreed Advisory Partners
Title: CEO

Address: 718 Quillmore Ave, Miami, Florida 33190

Target Market(s)

companies over 100 employees

Industry/Entity Type

Business

```html
<!DOCTYPE html>
<html lang="en">
<head>
<meta charset="utf-8">
<title>Tallowreed Advisory Partners – Business Card</title>
<link rel="stylesheet" href="https://fonts.googleapis.com/css2?family=Archivo:wght@400;700&display=swap">
<style>
  :root {
    --bg: #e9e6e2;
    --card: #ffffff;
    --brand-blue: #0a5cf5;
    --ink: #111111;
    --ink-soft: #333333;
    --shadow: rgba(0, 0, 0, 0.18);
  }
  * { box-sizing: border-box; margin: 0; padding: 0; }
  html, body {
    width: 1200px; height: 918px; overflow: hidden;
    background: var(--bg);
    font-family: "Archivo", Arial, sans-serif;
  }
  .sheet {
    position: relative; width: 1200px; height: 918px;
  }
  .card {
    position: absolute; left: 320px;
    width: 560px; height: 320px;
    background: var(--card);
    box-shadow: 0 6px 20px var(--shadow);
    overflow: hidden;
  }
  .card--contact { top: 110px; }
  .card--brand { top: 488px; }
  .card-bands {
    position: absolute; inset: 0; width: 100%; height: 100%;
  }
  .card-bands path { fill: var(--brand-blue); }

  /* Contact side */
  .brand-small {
    position: absolute; left: 34px; top: 30px;
    display: flex; align-items: center; gap: 10px;
  }
  .brand-dot {
    width: 30px; height: 30px; border-radius: 50%;
    background: var(--brand-blue);
  }
  .brand-name {
    font-weight: 700; color: var(--ink);
    letter-spacing: 0.06em; text-transform: uppercase;
  }
  .brand-small .brand-name { font-size: 13px; line-height: 1.15; width: 130px; }

  .contact {
    position: absolute; left: 300px; top: 96px;
    color: var(--ink-soft);
  }
  .contact-name {
    font-size: 21px; font-weight: 400; color: var(--ink);
  }
  .contact-title {
    font-size: 12px; font-style: italic; margin-bottom: 22px;
  }
  .contact-lines { list-style: none; font-size: 12px; line-height: 1.45; }

  /* Brand side */
  .brand-centre {
    position: absolute; left: 0; right: 0; top: 96px;
    display: flex; flex-direction: column; align-items: center; gap: 14px;
  }
  .brand-centre .brand-dot { width: 64px; height: 64px; }
  .brand-centre .brand-name {
    font-size: 26px; text-align: center; line-height: 1.15;
  }
</style>
</head>
<body>
<main class="sheet">

  <section class="card card--contact" aria-label="Business card, contact side">
    <svg class="card-bands" viewBox="0 0 560 320" preserveAspectRatio="none" aria-hidden="true">
      <path d="M0,50 C40,180 120,270 230,320 H172 C92,272 22,205 0,140 Z"/>
    </svg>
    <div class="brand-small">
      <span class="brand-dot"></span>
      <span class="brand-name">Tallowreed Advisory Partners</span>
    </div>
    <div class="contact">
      <p class="contact-name">Desmond Munkalt</p>
      <p class="contact-title">Chief Executive Officer</p>
      <ul class="contact-lines">
        <li>718 Quillmore Ave.</li>
        <li>Miami, Florida 33190</li>
        <li>Tel: 3055550148</li>
        <li>Mob: 9175550193</li>
        <li>dmunkalt@tallowreedadvisory.example</li>
        <li>www.tallowreedadvisory.example</li>
      </ul>
    </div>
  </section>

  <section class="card card--brand" aria-label="Business card, brand side">
    <svg class="card-bands" viewBox="0 0 560 320" preserveAspectRatio="none" aria-hidden="true">
      <path d="M0,0 H560 V92 Q330,22 0,6 Z"/>
      <path d="M0,238 Q280,262 560,300 V320 H0 Z"/>
    </svg>
    <div class="brand-centre">
      <span class="brand-dot"></span>
      <span class="brand-name">Tallowreed<br>Advisory Partners</span>
    </div>
  </section>

</main>
</body>
</html>
```